Flyer für Natur- und Chiropraxis
Zielgruppe
Natur- und Chiropraxis. (Berufsbild Heilpraktiker)
Ganzheitliche Chiropraktik und manuelle Gelenktherapie.
Patienten mit chronischen oder akuten Beschwerden des Halte- und Bewegungsapparates (z.b. Migräne+Spannungskopfschmerzen, Muskelkettendysbalancen, Bandscheibenvorfälle)
HWS und Atlastherapie (Bei Tinnitus, Schwindel, Kopfschmerzen)
Naturheilkunde und Vitalstoffinfusionen (Bei LongCovid und chronischem Erschöpfungssyndrom)
Extrakorporale Stoßwellentherapie ( Bei Fersensporn, Kalkschulter, Sehnenansatzentzündungen.)
Nebensächlich=Neuraltherapie, Extensionstherapie, Wärmetherapie, Magnetfeldtherapie, biologische Arthrosebehandlung, Dry-Needling Therapie.
Aufgabenstellung
Bitte das Heilmittelwerbegesetz beachten!
Geplanter start der Praxis 17.04.23
Adresse der Praxis= Lindenweg 7, 57312 Talbruck. Tel. 04567/73945

```html
<!DOCTYPE html>
<html lang="de">
<head>
<meta charset="utf-8">
<title>Flyer Natur- und Chiropraxis</title>
<link href="https://fonts.googleapis.com/css2?family=Federo&family=Montserrat:ital,wght@0,600;0,700;0,800;1,500;1,600;1,700&display=swap" rel="stylesheet">
<style>
  :root{
    --mint:#bdf2d2;
    --sky:#a9d3ea;
    --periwinkle:#8fb0f2;
    --green:#93c98e;
    --blue:#7590d6;
    --blue-head:#6f8ee0;
    --ink:#1d2140;
    --navy:#3b4c9e;
    --badge-navy:#1f2a78;
    --stage:#e4e4e4;
    --white:#ffffff;
  }
  *{box-sizing:border-box;margin:0;padding:0}
  html,body{width:1200px;height:900px;overflow:hidden;background:var(--stage)}
  body{font-family:'Federo',sans-serif;color:var(--ink);position:relative}

  .spread{position:absolute;top:150px;display:flex;box-shadow:0 10px 30px rgba(0,0,0,.15)}
  .spread--outside{left:40px}
  .spread--inside{left:630px}
  .panel{position:relative;width:265px;height:600px;overflow:hidden;
    background:linear-gradient(115deg,var(--mint) 0%,var(--sky) 50%,var(--periwinkle) 100%)}
  .photo{position:absolute}

  /* Welcome panel */
  .welcome__photo{left:0;top:0;width:265px;height:250px;
    background:linear-gradient(160deg,#d8d6d8 0%,#b9a894 45%,#5f6258 80%,#cfcacb 100%)}
  .welcome__house{position:absolute;left:0;top:185px;width:265px;height:415px;
    clip-path:polygon(0 14%,50% 0,100% 14%,100% 100%,0 100%);
    background:linear-gradient(200deg,var(--mint) 0%,var(--sky) 45%,var(--periwinkle) 100%)}
  .welcome__text{position:absolute;left:15px;top:266px;width:235px;text-align:center;font-size:19px;line-height:1.3}
  .badge-shadow{position:absolute;left:42px;top:392px;width:110px;height:136px;background:var(--blue)}
  .badge{position:absolute;left:30px;top:382px;width:110px;height:136px;background:var(--white);
    border-top:16px solid var(--badge-navy);border-bottom:8px solid var(--badge-navy)}
  .welcome__name{position:absolute;left:0;width:265px;top:540px;text-align:center;
    font-family:'Montserrat',sans-serif;font-weight:700;font-size:13px;color:#1f2a55}
  .contact{position:absolute;left:0;bottom:0;width:265px;height:36px;background:var(--green);
    display:flex;align-items:center;justify-content:space-around;padding:0 8px;
    font-family:'Montserrat',sans-serif;font-style:italic;font-weight:500;font-size:10px}
  .contact__item{display:flex;align-items:center;gap:5px}
  .contact__address{line-height:1.3}

  /* Cover panel */
  .brand{position:absolute;left:16px;top:14px;width:240px;display:flex;align-items:flex-start;gap:10px}
  .brand__dot{width:34px;height:34px;border-radius:50%;border:2px solid var(--blue);flex:none;margin-top:4px}
  .brand__name{flex:1;text-align:right;font-size:16px;line-height:1.2;color:var(--navy)}
  .cover__headline{position:absolute;left:0;width:265px;top:84px;text-align:center;
    font-family:'Montserrat',sans-serif;font-weight:800;font-size:26px;color:var(--blue-head);letter-spacing:-.5px}
  .cover__title{position:absolute;left:0;width:265px;top:124px;text-align:center;font-size:21px}
  .cover__note{position:absolute;left:0;width:265px;top:156px;text-align:center;
    font-family:'Montserrat',sans-serif;font-style:italic;font-weight:700;font-size:7px}
  .cover__spine{left:108px;top:188px;width:145px;height:300px;border-radius:26px;
    background:linear-gradient(180deg,#f3f3f3 0%,#e6ded0 50%,#efece6 100%)}
  .cover__rule{position:absolute;left:22px;top:250px;width:1px;height:200px;background:var(--blue)}
  .cover__massage{left:32px;top:290px;width:88px;height:100px;border-radius:8px;
    background:linear-gradient(150deg,#e4d4c0 0%,#c89a7c 50%,#4c3b32 100%)}
  .cover__date{position:absolute;left:28px;top:410px;font-family:'Montserrat',sans-serif;
    font-weight:700;font-size:23px;line-height:.9;color:var(--blue-head)}
  .cover__claim{position:absolute;left:18px;top:496px;width:185px;height:72px;background:var(--green);
    border-radius:0 26px 26px 0;display:flex;align-items:center;justify-content:center;
    text-align:center;font-size:13px;line-height:1.25}
  .cover__button{position:absolute;right:12px;bottom:6px;width:135px;height:36px;border-radius:14px;
    background:var(--blue);display:flex;align-items:center;justify-content:center;text-align:center;
    font-family:'Montserrat',sans-serif;font-weight:700;font-size:7.5px;color:var(--ink)}

  /* Inside panels */
  .inside__title{position:absolute;left:0;width:265px;top:18px;text-align:center;font-size:25px;line-height:1.3}
  .inside__text{position:absolute;text-align:center;font-size:12.5px;line-height:1.35}
  .offers__text{left:14px;width:237px;top:108px}
  .block{position:absolute}
  .frame{position:absolute;border:6px solid var(--white)}
  .inside__footer{position:absolute;left:0;bottom:0;height:95px;background:linear-gradient(90deg,var(--mint),var(--periwinkle))}
  .inside__caption{position:absolute;top:520px;text-align:center;font-size:13px;line-height:1.4}

  .offers__block-tall{left:8px;top:290px;width:52px;height:200px;background:var(--blue)}
  .offers__block-low{left:70px;top:410px;width:160px;height:92px;background:var(--blue)}
  .offers__photo-main{left:45px;top:280px;width:195px;height:145px;
    background:linear-gradient(150deg,#e6e3e1 0%,#b78c6e 50%,#9a2f2a 100%)}
  .offers__photo-small{left:22px;top:382px;width:120px;height:120px;
    background:linear-gradient(160deg,#c8a57a 0%,#8a6a4e 55%,#3f4a6a 100%)}
  .offers__footer{width:265px}
  .offers__caption{left:10px;width:245px}

  .more__label{position:absolute;left:6px;width:205px;top:14px;text-align:center;font-size:10.5px}
  .more__arrow{position:absolute;left:150px;top:36px}
  .more__text{left:6px;width:205px;top:118px}
  .more__block-tall{left:8px;top:290px;width:52px;height:190px;background:var(--green)}
  .more__block-low{left:70px;top:410px;width:135px;height:92px;background:var(--green)}
  .more__photo-main{left:42px;top:280px;width:168px;height:145px;
    background:linear-gradient(150deg,#5b5a52 0%,#d9d7d1 55%,#3c3b38 100%)}
  .more__photo-small{left:16px;top:382px;width:120px;height:120px;
    background:linear-gradient(160deg,#c3267a 0%,#d8b09a 45%,#8f6e5c 100%)}
  .more__footer{width:213px}
  .more__caption{left:5px;width:203px;font-size:12.5px}
  .more__band{position:absolute;right:0;top:56px;bottom:0;width:52px;background:var(--green)}
  .more__list{position:absolute;right:10px;top:66px;height:524px;writing-mode:vertical-rl;
    font-family:'Montserrat',sans-serif;font-style:italic;font-weight:600;font-size:10px;line-height:1.4}
</style>
</head>
<body>

<section class="spread spread--outside">
  <article class="panel welcome">
    <div class="photo welcome__photo" role="img" aria-label="Foto: Therapeut behandelt die Schulter einer Patientin"></div>
    <div class="welcome__house"></div>
    <p class="welcome__text">Ab dem 17.4.2023 heiße ich sie Herzlich Willkommen in meiner neuen Praxis</p>
    <div class="badge-shadow"></div>
    <div class="badge" role="img" aria-label="Zertifikat"></div>
    <p class="welcome__name">Dr.med. Jonas Wehrmann</p>
    <footer class="contact">
      <span class="contact__item">
        <svg width="14" height="20" viewBox="0 0 14 20" fill="none" stroke="#1d2140" stroke-width="1.3"><path d="M7 18.5C7 18.5 1 11 1 7a6 6 0 0 1 12 0c0 4-6 11.5-6 11.5z"/><circle cx="7" cy="7" r="2.3"/></svg>
        <span class="contact__address">Lindenweg 7<br>57312 Talbruck</span>
      </span>
      <span class="contact__item">
        <svg width="16" height="16" viewBox="0 0 24 24" fill="none" stroke="#1d2140" stroke-width="1.8"><path d="M5 3h4l2 5-2.5 1.5a11 11 0 0 0 6 6L16 13l5 2v4a2 2 0 0 1-2 2A17 17 0 0 1 3 5a2 2 0 0 1 2-2z"/></svg>
        04567/73945
      </span>
    </footer>
  </article>

  <article class="panel cover">
    <header class="brand">
      <span class="brand__dot"></span>
      <span class="brand__name">Dr.med.<br>Jonas Wehrmann</span>
    </header>
    <h1 class="cover__headline">NEUERÖFFNUNG</h1>
    <h2 class="cover__title">Natur und Chiropraxis</h2>
    <p class="cover__note">(Berufsbild Heilpraktiker)</p>
    <div class="photo cover__spine" role="img" aria-label="Foto: Modell einer Wirbelsäule"></div>
    <span class="cover__rule"></span>
    <div class="photo cover__massage" role="img" aria-label="Foto: Rückenmassage"></div>
    <p class="cover__date">17<br>APRIL<br>2023</p>
    <p class="cover__claim">Ganzheitliche Chiropraktik<br>und manuelle<br>Gelenktherapie.</p>
    <p class="cover__button">Unsere Therapieangebote<br>siehe Innenteil</p>
  </article>
</section>

<section class="spread spread--inside">
  <article class="panel offers">
    <h2 class="inside__title">Unsere<br>Therapieangebote</h2>
    <p class="inside__text offers__text">Patienten mit chronischen oder akuten Beschwerden des Halte- und Bewegungsapparates (z.b. Migräne+Spannungskopfschmerzen, Muskelkettendysbalancen, Bandscheibenvorfälle)</p>
    <div class="block offers__block-tall"></div>
    <div class="block offers__block-low"></div>
    <div class="photo offers__photo-main" role="img" aria-label="Foto: Frau mit Kopfschmerzen"></div>
    <div class="frame photo offers__photo-small" role="img" aria-label="Foto: Mann mit Nackenschmerzen"></div>
    <div class="inside__footer offers__footer"></div>
    <p class="inside__caption offers__caption">HWS und<br>Atlastherapie (Bei<br>Tinnitus, Schwindel,<br>Kopfschmerzen)</p>
  </article>

  <article class="panel more">
    <p class="more__label">Weitere Therapienebenangebote</p>
    <svg class="more__arrow" width="44" height="52" viewBox="0 0 44 52" fill="none" stroke="#7590d6" stroke-width="4" stroke-linecap="round"><path d="M14 4C2 16 8 38 32 44"/><path d="M24 34l9 10-12 4"/></svg>
    <p class="inside__text more__text">Naturheilkunde und Vitalstoffinfusionen (Bei LongCovid und chronischem Erschöpfungssyndrom)</p>
    <div class="block more__block-tall"></div>
    <div class="block more__block-low"></div>
    <div class="photo more__photo-main" role="img" aria-label="Foto: erschöpfte Frau am Tisch"></div>
    <div class="frame photo more__photo-small" role="img" aria-label="Foto: Hand auf einer Schulter"></div>
    <div class="inside__footer more__footer"></div>
    <p class="inside__caption more__caption">Extrakorporale Stoßwellentherapie ( Bei Fersensporn, Kalkschulter, Sehnenansatzentzündungen.)</p>
    <div class="more__band"></div>
    <p class="more__list">Neuraltherapie, Extensionstherapie, Wärmetherapie, Magnetfeldtherapie, biologische Arthrosebehandlung, Dry-Needling Therapie.</p>
  </article>
</section>

</body>
</html>
```